Brake Test Training for Coal Mining

We offer Brake Test Training for Coal Mine workers. It's a legislative requirement that workers who are tasked with performing brake testing have certain competencies to do so. We test Light Vehicles and trailers, Heavy Vehicles and Mobile Mining Equipment like Graders, Scrapers and Dump Trucks.

```html
<!DOCTYPE html>
<html lang="en">
<head>
<meta charset="UTF-8">
<title>Ridgeline Operator Training – Brake Test Training</title>
<link rel="stylesheet" href="https://fonts.googleapis.com/css2?family=Bebas+Neue&family=Montserrat:wght@800&display=swap">
<style>
  :root {
    --navy: #0c3460;
    --gold: #f0b400;
    --paper: #f6f6f4;
    --page: #e9ebee;
    --white: #ffffff;
  }
  * { margin: 0; padding: 0; box-sizing: border-box; }
  html, body {
    width: 1200px;
    height: 1095px;
    overflow: hidden;
    background: var(--page);
  }
  .billboard {
    position: absolute;
    left: 0;
    top: 291px;
    width: 1200px;
    height: 512px;
    background: var(--paper);
    overflow: hidden;
  }
  .billboard__shapes {
    position: absolute;
    inset: 0;
  }
  .brand {
    position: absolute;
    left: 140px;
    top: 62px;
    display: flex;
    align-items: center;
    gap: 18px;
  }
  .brand__dot {
    width: 70px;
    height: 70px;
    border-radius: 50%;
    background: var(--navy);
    flex: none;
  }
  .brand__name {
    font-family: "Bebas Neue", sans-serif;
    font-size: 38px;
    line-height: 0.98;
    letter-spacing: 1px;
    color: var(--navy);
  }
  .headline {
    position: absolute;
    left: 18px;
    top: 218px;
    width: 600px;
    text-align: center;
    font-family: "Bebas Neue", sans-serif;
    font-weight: 400;
    line-height: 1;
    white-space: nowrap;
  }
  .headline__lead {
    display: block;
    font-size: 64px;
    color: var(--navy);
    letter-spacing: -0.5px;
  }
  .headline__accent {
    display: block;
    margin-top: 10px;
    font-size: 62px;
    color: var(--gold);
    letter-spacing: -0.5px;
  }
  .phone {
    position: absolute;
    left: 42px;
    top: 447px;
    display: flex;
    align-items: center;
    gap: 20px;
  }
  .phone__icon {
    width: 52px;
    height: 52px;
  }
  .phone__number {
    font-family: "Montserrat", sans-serif;
    font-weight: 800;
    font-size: 44px;
    color: var(--white);
    letter-spacing: 1px;
  }
</style>
</head>
<body>
  <section class="billboard">
    <svg class="billboard__shapes" width="1200" height="512" viewBox="0 0 1200 512">
      <defs>
        <linearGradient id="site-photo-tone" x1="0" y1="0" x2="0" y2="1">
          <stop offset="0" stop-color="#cfcdd3"/>
          <stop offset="0.22" stop-color="#c2bcbd"/>
          <stop offset="0.34" stop-color="#b08a5c"/>
          <stop offset="0.48" stop-color="#d99a2a"/>
          <stop offset="0.66" stop-color="#c88a24"/>
          <stop offset="0.8" stop-color="#6f5f52"/>
          <stop offset="0.88" stop-color="#a59a8f"/>
          <stop offset="1" stop-color="#b6aea6"/>
        </linearGradient>
      </defs>
      <polygon class="stripe-navy" points="796,0 808,0 690,512 628,512" fill="var(--navy)"/>
      <polygon class="stripe-gold" points="808,0 816,0 712,512 690,512" fill="var(--gold)"/>
      <polygon class="site-photo" role="img" aria-label="Photo of a large yellow mining dump truck loaded with ore on a quarry haul road"
               points="816,0 1200,0 1200,512 712,512" fill="url(#site-photo-tone)"/>
      <polygon class="phone-band" points="0,436 555,436 530,512 0,512" fill="var(--navy)"/>
    </svg>

    <div class="brand">
      <span class="brand__dot"></span>
      <span class="brand__name">Ridgeline<br>Operator Training</span>
    </div>

    <h1 class="headline">
      <span class="headline__lead">Training and Experience</span>
      <span class="headline__accent">You Can Rely On</span>
    </h1>

    <div class="phone">
      <svg class="phone__icon" viewBox="0 0 54 54" aria-hidden="true">
        <circle cx="27" cy="27" r="27" fill="var(--gold)"/>
        <path d="M19.5 14.5c1.2-.8 2.6-.5 3.4.6l2.6 3.7c.7 1 .6 2.4-.3 3.2l-1.7 1.5c1.3 3 3.6 5.5 6.6 7l1.6-1.7c.8-.9 2.2-1 3.2-.3l3.7 2.6c1.1.8 1.4 2.3.6 3.4l-1.6 2.3c-1 1.4-2.8 2-4.4 1.5-8.3-2.5-14.6-9-16.9-17.3-.4-1.6.2-3.3 1.6-4.3z" fill="var(--navy)"/>
      </svg>
      <span class="phone__number">07 5310 8826</span>
    </div>
  </section>
</body>
</html>
```